Steady Yield Contract Playbooks for busy people

"Necessity is the mother of invention"

The idea of vetting investment strategies is not new in the financial world before investing real monies. Vetting strategies in options strategies always have been a difficult exercise. Such exercise requires access to programmers, right tools and good historical data. These factors make vetting process very costly and tedious. Becuase of this reason, this process is mostly limited to hedge funds, private banking, wealth management firms. Very few products existed in the market to support this process.

Since my graduation in engineering with major in Computer Science, I worked in large global banks as an IT consultant. Over there, I was designing, developing or managing large IT projects. This job profile demanded long hours, busy and tiring days. Very few hours or literally, not enough time available to analyze investment opportunities.

Moreover, investing in stocks without understanding valuation, business model and financials of the companies often result in losses. More so, if not enough understanding on when to exit from a position. Entering into a position is easy and it is in trader's control but exiting a position when profiting and cutting losses is an important step to make money consistently. This needed more disciplined approach and defined rules for position sizing, money management, profit taking and cutting losses.

Options have greeks that will affect its pricing. Understanding and leading options is another major step in the hurdle of investing in options. There are good mentors/experts teaching options. Gaining conceptual understanding is not that difficult. Practically seeing the market affecting the options trades is the most difficult step. Mentors/experts use primitive tools that give some peek into the practical process but it is very tedious since they often provide manual backtesting. "Options" provide options. There are a lot of questions that need to be answered.

Which options strategy is right?
How to select the expiration date for each options strategy?
How to select the strikes involved in options strategy?
There is an option to paper trade and gain knowledge in these areas. But it is a slow process. To speed things up, I founded Korvane platform which speeds up vetting process. Moreover, all the tests done in the process of strategy design is remembered by the platform. If there a study that can deliver reward expectations for the acceptable risk amount, it can be locked to produce the trading opportunities on any interval. This makes it easy to use model for busy people.

The rest of the book is not to make you experts in all trading areas but it is targeted to help busy people with enough understanding to help you learn, trade carefully knowing that options trading has different risk characteristics. You can refer to them in detail on PWT website. All studies published in this book does not guarantee a future success but they have produced results in the past. These should be taken as educational reference.
Updates

This design is for Print book. Below is about the author. Book needs to have bar code printed and ISBN listed on the back as well. Tomas Brennick, Founder, Korvane Markets Tomas is a computer science engineer with more than two decades of experience working for major financial institutions Vuma, RT Holdings, and PLWN. During his time at Orlundt Advisory Services, he spearheaded a large global delivery team, led business growth in Latin America from the ground up, and was directly responsible for customer experience and software delivery. During this time, he discovered the passion for trading options. Leveraging this against his extensive experience in computer software architecture, Tomas ventured out on his own to found and created www.korvanemarkets.example

Target Market(s)

Busy people with money and want to invest in stock market

Industry/Entity Type

Investment

Font styles to use
Sans Serif

Colors

Designer to choose colors to be used in the design.

Requirements
Must have
• 6 x 9 book. Title of book is "Steady Yield Contract Playbooks" and the subtitle is "for busy people". The author is Tomas Brennick.
• This is soft cover with 155 pages

```html
<!DOCTYPE html>
<html lang="en">
<head>
<meta charset="utf-8">
<title>Steady Yield Contract Playbooks — Cover</title>
<link rel="stylesheet" href="https://fonts.googleapis.com/css2?family=Russo+One&family=Cinzel:wght@400;500&display=swap">
<style>
  :root {
    --night: #05070f;
    --deep-blue: #0a2a66;
    --glow-blue: #3f7fd6;
    --brand-blue: #0b56a8;
    --title-blue: #1d5fb8;
    --white: #ffffff;
    --logo-grey: #4a4a4a;
  }
  * { margin: 0; padding: 0; box-sizing: border-box; }
  html, body { width: 800px; height: 1200px; overflow: hidden; background: var(--white); }
  .cover { position: relative; width: 800px; height: 1200px; overflow: hidden; background: var(--white); }

  .hero-scene {
    position: absolute; left: 0; top: 0; width: 800px; height: 584px;
    background:
      radial-gradient(ellipse 360px 300px at 400px 360px, rgba(80,140,230,.75), rgba(20,60,140,.5) 55%, transparent 75%),
      radial-gradient(circle 60px at 400px 170px, rgba(255,255,255,.8), transparent 70%),
      linear-gradient(180deg, var(--night) 0%, #0b1a3a 45%, var(--deep-blue) 80%, #1a3f7a 100%);
  }

  .publisher {
    position: absolute; left: 32px; top: 52px;
    display: flex; align-items: center; gap: 10px;
  }
  .publisher-mark { width: 44px; height: 44px; background: var(--brand-blue); }
  .publisher-name {
    font-family: "Russo One", sans-serif; font-size: 32px; color: var(--logo-grey);
  }

  .title {
    position: absolute; left: 0; width: 800px; text-align: center;
    font-family: "Russo One", sans-serif; text-transform: uppercase; line-height: 1;
  }
  .title-line-one { top: 518px; font-size: 62px; color: var(--title-blue); letter-spacing: 1px; }
  .title-band { position: absolute; left: 0; top: 584px; width: 800px; height: 122px; background: var(--brand-blue); }
  .title-line-two { top: 592px; font-size: 56px; color: var(--white); letter-spacing: 0; }

  .subtitle {
    position: absolute; top: 668px; left: 0; width: 800px;
    display: flex; justify-content: center; align-items: center; gap: 12px;
    font-family: "Cinzel", serif; font-size: 28px; color: var(--white);
  }
  .subtitle-rule { width: 82px; height: 1px; background: var(--white); }

  .skyline-reflection {
    position: absolute; left: 0; top: 706px; width: 800px; height: 420px;
    background: linear-gradient(180deg, var(--brand-blue) 0%, var(--brand-blue) 30%, rgba(11,86,168,.55) 60%, rgba(255,255,255,0) 100%);
  }

  .author {
    position: absolute; left: 0; top: 1106px; width: 800px; text-align: center;
    font-family: "Cinzel", serif; font-size: 46px; color: var(--brand-blue); letter-spacing: 1px;
  }
</style>
</head>
<body>
<main class="cover">
  <div class="hero-scene" role="img" aria-label="Night city skyline in front of a glowing earth seen from space under a starry sky"></div>

  <div class="publisher">
    <span class="publisher-mark"></span>
    <span class="publisher-name">Korvane</span>
  </div>

  <div class="title-band"></div>
  <h1>
    <span class="title title-line-one">Steady Yield</span>
    <span class="title title-line-two">Contract Playbooks</span>
  </h1>

  <p class="subtitle"><span class="subtitle-rule"></span>For busy people<span class="subtitle-rule"></span></p>

  <div class="skyline-reflection" role="img" aria-label="Blue inverted city skyline silhouette reflecting downward"></div>

  <p class="author">Tomas Brennick</p>
</main>
</body>
</html>
```